Email Signature Block Design for Law Firm

I would like you to create a similar signature block for my law firm . I saw the email signature block attached as image002.png and wanted a similar design for my law firm. I want to be able to swap the portraits for each of my staff from the final design. Our law firm colors are black, gold, white, red.

Law

• i like the red circle in around the photo in the oak ridge guild design. The Tall Cedar Guild desgn is what inspired me to have a signature block design for my firm.

```html
<!DOCTYPE html>
<html lang="en">
<head>
<meta charset="utf-8">
<title>Tall Cedar Guild – Email Signature</title>
<link rel="stylesheet" href="https://fonts.googleapis.com/css2?family=Cinzel:wght@600;700&family=Poppins:wght@400;500;600&family=Montserrat:wght@500;800&display=swap">
<style>
  :root {
    --gold: #d9982a;
    --gold-faint: #f8ecd6;
    --black: #161616;
    --white: #ffffff;
    --ink: #111111;
    --stage: #c4c4c4;
    --photo-a: #e8e8e8;
    --photo-b: #2a2a2a;
  }
  * { margin: 0; padding: 0; box-sizing: border-box; }
  html, body { width: 1200px; height: 366px; overflow: hidden; background: var(--stage); }
  .signature {
    position: absolute; left: 0; top: 44px;
    width: 1200px; height: 277px;
    background: var(--white);
    overflow: visible;
  }
  .brand-mark {
    position: absolute; left: 30px; top: 32px;
    width: 58px; height: 58px; background: var(--gold);
  }
  .firm-name {
    position: absolute; left: 105px; top: 44px;
    font-family: "Cinzel", serif; font-weight: 600;
    font-size: 22px; color: var(--ink); letter-spacing: 0.5px; white-space: nowrap;
  }
  .firm-tagline {
    position: absolute; left: 105px; top: 76px; width: 272px;
    display: flex; align-items: center; gap: 6px;
    font-family: "Montserrat", sans-serif; font-weight: 800;
    font-size: 8px; letter-spacing: 5px; color: var(--ink); white-space: nowrap;
  }
  .firm-tagline::before, .firm-tagline::after {
    content: ""; flex: 1; height: 1px; background: var(--ink);
  }
  .person-name {
    position: absolute; left: 25px; top: 121px;
    font-family: "Cinzel", serif; font-weight: 700;
    font-size: 35px; line-height: 1; color: var(--ink); white-space: nowrap;
  }
  .person-role {
    position: absolute; left: 25px; top: 158px;
    font-family: "Poppins", sans-serif; font-weight: 400;
    font-size: 20px; line-height: 1; color: var(--ink);
  }
  .social-band {
    position: absolute; left: 0; bottom: 0; width: 100%; height: 62px;
    background: var(--black);
  }
  .follow-label {
    position: absolute; left: 23px; top: 12px;
    font-family: "Montserrat", sans-serif; font-weight: 500;
    font-size: 14px; letter-spacing: 3.5px; color: var(--white);
  }
  .social-links { position: absolute; left: 226px; top: 10px; display: flex; gap: 17px; }
  .social-links span {
    width: 19px; height: 19px; border-radius: 50%; background: var(--gold); display: block;
  }
  .website {
    position: absolute; right: 28px; top: 3px;
    font-family: "Montserrat", sans-serif; font-weight: 800;
    font-size: 23px; letter-spacing: 4.4px; color: var(--white);
  }
  .portrait-ring { position: absolute; left: 496px; top: 27px; }
  .contact-list {
    position: absolute; left: 748px; top: 74px; list-style: none;
    font-family: "Poppins", sans-serif; font-weight: 500;
    font-size: 19.5px; line-height: 21px; color: var(--ink);
  }
  .contact-list li { display: flex; align-items: flex-start; gap: 9px; margin-bottom: 14px; }
  .contact-list li.address { margin-bottom: 12px; }
  .contact-icon {
    flex: none; width: 23px; height: 23px; border-radius: 50%;
    background: var(--gold); display: flex; align-items: center; justify-content: center;
  }
  .contact-list li span.text { padding-left: 6px; }
  .watermark-shape {
    position: absolute; left: 1058px; top: 68px;
    width: 112px; height: 112px; background: var(--gold-faint);
  }
</style>
</head>
<body>
<main class="signature">
  <div class="watermark-shape" aria-hidden="true"></div>

  <div class="brand-mark" aria-hidden="true"></div>
  <div class="firm-name">Tall Cedar Guild, PLLC</div>
  <div class="firm-tagline">Attorneys At Law</div>

  <h1 class="person-name">MARCUS D. HALE</h1>
  <p class="person-role">Personal Injury Lawyer</p>

  <div class="social-band">
    <span class="follow-label">FOLLOW US ON</span>
    <div class="social-links" aria-label="Social profiles">
      <span></span><span></span><span></span><span></span><span></span>
    </div>
    <div class="website">www.tallcedarguild.com</div>
  </div>

  <svg class="portrait-ring" width="214" height="214" viewBox="0 0 214 214">
    <defs>
      <linearGradient id="photoTone" x1="0" y1="0" x2="0" y2="1">
        <stop offset="0" stop-color="var(--photo-a)"/>
        <stop offset="0.55" stop-color="#bdbdbd"/>
        <stop offset="1" stop-color="var(--photo-b)"/>
      </linearGradient>
    </defs>
    <circle cx="107" cy="107" r="88" fill="var(--white)"/>
    <circle cx="107" cy="107" r="83" fill="url(#photoTone)" role="img" aria-label="Portrait photo of the attorney in a dark suit"/>
    <path d="M 58 23 A 98 98 0 0 1 200 138" fill="none" stroke="var(--gold)" stroke-width="14"/>
    <path d="M 164 186 A 98 98 0 0 1 12 84" fill="none" stroke="var(--gold)" stroke-width="14"/>
  </svg>

  <ul class="contact-list">
    <li>
      <span class="contact-icon"><svg width="12" height="12" viewBox="0 0 24 24"><path d="M6.6 10.8a15 15 0 0 0 6.6 6.6l2.2-2.2a1 1 0 0 1 1-.25 11.4 11.4 0 0 0 3.6.57 1 1 0 0 1 1 1V20a1 1 0 0 1-1 1A17 17 0 0 1 3 4a1 1 0 0 1 1-1h3.5a1 1 0 0 1 1 1c0 1.25.2 2.45.57 3.57a1 1 0 0 1-.25 1z" fill="#fff"/></svg></span>
      <span class="text">555-010-4827</span>
    </li>
    <li class="address">
      <span class="contact-icon"><svg width="12" height="12" viewBox="0 0 24 24"><path d="M12 2a7 7 0 0 0-7 7c0 5.25 7 13 7 13s7-7.75 7-13a7 7 0 0 0-7-7zm0 9.5A2.5 2.5 0 1 1 12 6.5a2.5 2.5 0 0 1 0 5z" fill="#fff"/></svg></span>
      <span class="text">412 N Harbor Ave. Suite 110<br>Bayview, FL 32599</span>
    </li>
    <li>
      <span class="contact-icon"><svg width="13" height="13" viewBox="0 0 24 24"><rect x="3" y="5" width="18" height="14" rx="1.5" fill="none" stroke="#fff" stroke-width="2"/><path d="M3.5 6l8.5 7 8.5-7" fill="none" stroke="#fff" stroke-width="2"/></svg></span>
      <span class="text">info@tallcedarguild.com</span>
    </li>
  </ul>
</main>
</body>
</html>
```